Design a wedding invitation

I need a classic and beautiful wedding invitation design URGENTLY
I have uploaded some example invitations where I like the LAYOUT only - PLESE REFER TO THIS LAYOUT FOR IMAGE, LOGO AND TEXT !
The imagery is in the other file uploaded - there are two options for the imagery whichever one works best with the layout
I would like to include some sort of logo of our initials H&L if possible
Size is A5
I would like to keep the same colour palette as the artworks
I do not want to make the Vantrel Arch the centre of the design we are looking for a more subtle effect
We want to avoid the look of 'image at the bottom and text at the top' by creating one unified piece
The final design will be letterpress printed with embossing so image cannot overlap with text
The wording is as follows:

“The honour of your presence
is requested at the wedding of Lucinda Marsh to Henrik Dalvang
Saturday, the eighth of September Two thousand and eighteen
at six o’clock in the evening
Château du Q
Paris, France
Black Tie"

```html
<!DOCTYPE html>
<html lang="en">
<head>
<meta charset="utf-8">
<title>Wedding Invitation – Lucinda Marsh &amp; Henrik Dalvang</title>
<link rel="stylesheet" href="https://fonts.googleapis.com/css2?family=Cinzel:wght@400&family=Great+Vibes&display=swap">
<style>
  :root {
    --page: #ffffff;
    --ink: #2a2426;
    --rose: #c95f7c;
    --mist: #eef0f2;
    --paper-warm: #f5f1ef;
    --paper-grey: #eeeeee;
    --garden-top: rgba(226, 182, 194, 0);
    --garden-mid: #e6c3cc;
    --garden-low: #d7b9cf;
    --street-top: rgba(190, 186, 188, 0);
    --street-mid: #cdbfc3;
    --street-low: #9b9798;
    --serif: "Cinzel", "Times New Roman", serif;
    --script: "Great Vibes", cursive;
  }
  * { box-sizing: border-box; margin: 0; padding: 0; }
  html, body {
    width: 1200px; height: 855px; overflow: hidden;
    background: var(--page);
  }
  .showcase { position: relative; width: 1200px; height: 855px; }

  .invitation {
    position: absolute; top: 49px;
    width: 535px; height: 760px;
    overflow: hidden;
    box-shadow: 0 2px 8px rgba(0,0,0,.18);
    color: var(--ink);
  }
  .invitation--garden { left: 47px; background: linear-gradient(180deg, var(--mist) 0%, var(--paper-warm) 55%, #f7eef0 100%); }
  .invitation--street { left: 623px; background: linear-gradient(180deg, #f3f3f3 0%, var(--paper-grey) 60%, #e8e8e8 100%); }

  .scene { position: absolute; left: 0; right: 0; bottom: 0; }
  .scene--garden {
    top: 515px;
    background: linear-gradient(180deg, var(--garden-top) 0%, var(--garden-mid) 30%, var(--garden-low) 100%);
  }
  .scene--street {
    top: 470px;
    background: linear-gradient(180deg, var(--street-top) 0%, var(--street-mid) 30%, var(--street-low) 100%);
  }

  .frame { position: absolute; inset: 0; width: 535px; height: 760px; }

  .monogram {
    position: absolute; left: 208px; top: 4px;
    width: 120px; height: 120px;
    border: 2px solid var(--rose); border-radius: 50%;
    background: inherit;
    display: flex; align-items: center; justify-content: center;
    font-family: var(--serif); font-size: 26px; color: var(--rose);
    letter-spacing: 1px;
  }

  .line { position: absolute; left: 0; width: 100%; text-align: center; line-height: 1; }
  .line--caps { font-family: var(--serif); font-size: 15.5px; letter-spacing: .4px; }
  .line--name { font-family: var(--script); font-size: 42px; }
  .line--joiner { font-family: var(--serif); font-size: 14px; color: var(--rose); }
  .line--dress { font-family: var(--script); font-size: 36px; }
</style>
</head>
<body>
<main class="showcase">

  <section class="invitation invitation--garden">
    <div class="scene scene--garden" role="img" aria-label="Painted riverside scene in soft pink and lilac: the Vantrel Arch on the left, a blossoming tree on the right, a couple strolling by a lamp post and bridge"></div>
    <svg class="frame" viewBox="0 0 535 760" aria-hidden="true">
      <g stroke="var(--rose)" stroke-width="1.5" fill="none">
        <line x1="14" y1="20" x2="200" y2="20"/>
        <line x1="336" y1="20" x2="521" y2="20"/>
        <line x1="20" y1="20" x2="20" y2="500"/>
        <line x1="515" y1="20" x2="515" y2="300"/>
      </g>
    </svg>
    <div class="monogram">H&amp;L</div>
    <p class="line line--caps" style="top:152px">The honour of your presence</p>
    <p class="line line--caps" style="top:172px">is requested at the wedding of</p>
    <p class="line line--name" style="top:206px">Lucinda Marsh</p>
    <p class="line line--joiner" style="top:262px">TO</p>
    <p class="line line--name" style="top:276px">Henrik Dalvang</p>
    <p class="line line--caps" style="top:326px">Saturday</p>
    <p class="line line--caps" style="top:346px">September 8th, 2018</p>
    <p class="line line--caps" style="top:385px">At 6 in the evening</p>
    <p class="line line--caps" style="top:421px">Château du Q</p>
    <p class="line line--caps" style="top:442px">Paris, France</p>
    <p class="line line--dress" style="top:472px">Black Tie</p>
  </section>

  <section class="invitation invitation--street">
    <div class="scene scene--street" role="img" aria-label="Painted Paris street in grey with pink blossom trees, lamp posts, a couple walking and the Vantrel Arch in the distance"></div>
    <svg class="frame" viewBox="0 0 535 760" aria-hidden="true">
      <g stroke="var(--rose)" stroke-width="1.5" fill="none">
        <line x1="14" y1="20" x2="200" y2="20"/>
        <line x1="336" y1="20" x2="521" y2="20"/>
        <line x1="20" y1="20" x2="20" y2="425"/>
        <line x1="515" y1="20" x2="515" y2="425"/>
      </g>
    </svg>
    <div class="monogram">H&amp;L</div>
    <p class="line line--caps" style="top:136px">The honour of your presence</p>
    <p class="line line--caps" style="top:156px">is requested at the wedding of</p>
    <p class="line line--name" style="top:180px">Lucinda Marsh</p>
    <p class="line line--joiner" style="top:227px">TO</p>
    <p class="line line--name" style="top:246px">Henrik Dalvang</p>
    <p class="line line--caps" style="top:293px">Saturday</p>
    <p class="line line--caps" style="top:313px">September 8th, 2018</p>
    <p class="line line--caps" style="top:348px">At 6 in the evening</p>
    <p class="line line--caps" style="top:384px">Château du Q</p>
    <p class="line line--caps" style="top:405px">Paris, France</p>
    <p class="line line--dress" style="top:428px">Black Tie</p>
  </section>

</main>
</body>
</html>
```